Chestnut Farm Logo and Business Card

We need a new logo design and new business cards for a recently purchased mature Chestnut Farm in the south west of Western Australia, the farm is called Willowmere Glen, We will be adding value to the chestnuts by creating a range of chestnut products based on the fact that chestnuts are a healthy, gluten free product that is suited to the vegetarian market as well as the health food market. We will be selling the products through farmers markets, restaurants, health food stores and online. The final design should communicate a healthy modern down to earth image.
Updates

Sorry, I should have given the details for the business cards.

Address is 
Willowmere Glen
PO Box 417 
Tallowbrook, Western Australia, 6318

Email is 
willowmere.glen@fernpost.com

Website is
www.glenhollowfoods.com

Phone number is 
(08) 9412 7730

Many thanks

We would like to see the logo separate to the business card as well if possible please?

Industry/Entity Type

Farm

Logo Text

Willowmere Glen

```html
<!DOCTYPE html>
<html lang="en">
<head>
<meta charset="utf-8">
<title>Willowmere Glen — Business Card</title>
<link href="https://fonts.googleapis.com/css2?family=Playfair+Display:wght@400;600&family=Libre+Baskerville&display=swap" rel="stylesheet">
<style>
  :root {
    --backdrop: #e6e4e1;
    --card-white: #ffffff;
    --bark: #3a2214;
    --bark-deep: #2f1a0e;
    --gold: #c9a227;
    --cream: #fbf6ec;
  }
  * { box-sizing: border-box; margin: 0; padding: 0; }
  html, body { width: 1200px; height: 1023px; overflow: hidden; }
  body {
    background: var(--backdrop);
    position: relative;
    font-family: "Libre Baskerville", Georgia, serif;
  }
  .card {
    position: absolute;
    left: 240px; top: 180px;
    width: 720px; height: 400px;
    background: var(--card-white);
    box-shadow: 0 14px 34px rgba(0,0,0,.22);
    overflow: hidden;
  }
  .card-brand {
    position: absolute; left: 0; top: 0; width: 100%; height: 218px;
    display: flex; align-items: center; justify-content: center; gap: 16px;
  }
  .brand-dot { width: 22px; height: 22px; border-radius: 50%; background: var(--gold); }
  .brand-name {
    font-family: "Playfair Display", Georgia, serif;
    font-weight: 600; font-size: 44px; letter-spacing: 1px;
    color: var(--bark);
  }
  .card-rule { position: absolute; left: 0; top: 218px; width: 100%; height: 10px; background: var(--gold); }
  .card-details {
    position: absolute; left: 0; top: 228px; width: 100%; height: 172px;
    background: linear-gradient(180deg, var(--bark) 0%, var(--bark-deep) 100%);
    color: var(--cream);
    display: flex; justify-content: space-between;
    padding: 48px 46px 0 46px;
  }
  .person-name {
    font-family: "Playfair Display", Georgia, serif;
    font-size: 25px; letter-spacing: .5px; margin-bottom: 12px;
  }
  .contact-line { display: flex; align-items: center; gap: 8px; font-size: 15px; margin-bottom: 10px; }
  .icon { width: 20px; height: 20px; flex: none; }
  .address { display: flex; gap: 12px; font-size: 17px; line-height: 27px; margin-top: -4px; }
  .address .icon { margin-top: 4px; }
  .logo-band {
    position: absolute; left: 0; top: 870px; width: 1200px; height: 153px;
    background: var(--bark);
    display: flex; align-items: center; padding-left: 32px; gap: 14px;
  }
  .logo-band .brand-name { color: var(--card-white); font-size: 34px; }
  .logo-band .brand-dot { width: 18px; height: 18px; }
</style>
</head>
<body>
  <section class="card" aria-label="Business card front">
    <div class="card-brand">
      <span class="brand-dot"></span>
      <span class="brand-name">WILLOWMERE GLEN</span>
    </div>
    <div class="card-rule"></div>
    <div class="card-details">
      <div class="contact">
        <p class="person-name">MARA ELLISON</p>
        <p class="contact-line">
          <svg class="icon" viewBox="0 0 20 20"><circle cx="10" cy="10" r="10" fill="#c9a227"/><path d="M7 5.5l2 2-1 1.3c.6 1.4 1.8 2.6 3.2 3.2l1.3-1 2 2-1.2 1.5c-3.6-.6-6.4-3.4-7-7z" fill="#3a2214"/></svg>
          +61 (0) 8 9412 7730
        </p>
        <p class="contact-line">
          <svg class="icon" viewBox="0 0 20 20"><circle cx="10" cy="10" r="10" fill="#c9a227"/><rect x="5" y="6.5" width="10" height="7" fill="#3a2214"/><path d="M5 6.5l5 4 5-4" stroke="#c9a227" stroke-width="1" fill="none"/></svg>
          mara@maraellison.com.au
        </p>
      </div>
      <div class="address">
        <svg class="icon" viewBox="0 0 20 20"><circle cx="10" cy="10" r="10" fill="#c9a227"/><path d="M10 4.5a3.5 3.5 0 0 0-3.5 3.5c0 2.6 3.5 6.5 3.5 6.5s3.5-3.9 3.5-6.5A3.5 3.5 0 0 0 10 4.5z" fill="#fff"/><circle cx="10" cy="8" r="1.3" fill="#c9a227"/></svg>
        <p>Willowmere Glen<br>PO Box 417 Tallowbrook<br>Western Australia 6318<br>Australia</p>
      </div>
    </div>
  </section>

  <footer class="logo-band" aria-label="Logo on dark background">
    <span class="brand-dot"></span>
    <span class="brand-name">WILLOWMERE GLEN</span>
  </footer>
</body>
</html>
```